Business Card Design Project - Brantwell Media

We need a new business card that fits with our new logo. We are a social media agency and consultancy operating in China. We want a fresh and strong business card. Our cards need to be two-sided as we have both English and Chinese language names and addresses on the card, but as with our current business card this does not need to be a mirror-image. Our thoughts go out to a white card on the front where the logo/name is and then using the logo colours for different coloured back-grounds. i.e that the back of the biz card works with the four different colours in the logo.

Attached is the new logo, and also a copy of our old business cards.

Target Market(s)

CEO's, CMO's. media and advertising professionals

Industry/Entity Type

Business

Requirements
Must have
• inclusion of both Chinese and English language
Nice to have
• four different colored versions of the back of the biz card. Our logo has four colors and each of these colors we would like to have a version of.

```html
<!DOCTYPE html>
<html lang="en">
<head>
<meta charset="utf-8">
<title>Brantwell Media – Business Card</title>
<link href="https://fonts.googleapis.com/css2?family=Questrial&family=Noto+Sans+SC:wght@400;700&display=swap" rel="stylesheet">
<style>
  :root {
    --stage: #1f1f1f;
    --card: #f7f6f3;
    --ink: #231f20;
    --label: #ffffff;
    --green: #8dc63f;
    --purple: #6a2c91;
    --magenta: #ec008c;
    --orange: #f26522;
  }
  * { margin: 0; padding: 0; box-sizing: border-box; }
  html, body { width: 1200px; height: 900px; overflow: hidden; background: var(--stage); }
  body { position: relative; font-family: "Questrial", "Noto Sans SC", sans-serif; color: var(--ink); }

  .side-label { position: absolute; left: 105px; color: var(--label); font-size: 25px; letter-spacing: 0.5px; }
  .side-label--front { top: 56px; }
  .side-label--back { top: 518px; }

  .card { position: absolute; left: 308px; width: 766px; height: 417px; background: var(--card); border-radius: 4px; }
  .card--front { top: 18px; }
  .card--back { top: 465px; }

  .wordmark { position: absolute; display: flex; align-items: center; color: var(--ink); white-space: nowrap; }
  .wordmark__square { display: block; background: var(--purple); }
  .wordmark--front { left: 0; right: 0; top: 178px; justify-content: center; font-size: 56px; gap: 16px; }
  .wordmark--front .wordmark__square { width: 16px; height: 16px; }
  .wordmark--back { left: 66px; top: 60px; font-size: 30px; gap: 9px; }
  .wordmark--back .wordmark__square { width: 9px; height: 9px; }

  .swatches { position: absolute; display: flex; flex-direction: column; gap: 14px; }
  .swatches--right { left: 726px; top: 36px; }
  .swatches--left { left: 16px; top: 255px; }
  .swatch { width: 21px; height: 21px; }
  .swatch--green { background: var(--green); }
  .swatch--purple { background: var(--purple); }
  .swatch--magenta { background: var(--magenta); }
  .swatch--orange { background: var(--orange); }

  .contact { position: absolute; left: 284px; top: 163px; font-size: 13px; line-height: 18.5px; }
  .contact__name { color: var(--purple); font-size: 14px; }
  .contact__title { color: var(--green); font-size: 14px; }
  .contact__cn { font-family: "Noto Sans SC", sans-serif; font-weight: 700; font-size: 11px; }
  .hl-orange { color: var(--orange); }
  .hl-magenta { color: var(--magenta); }

  .cn-name { position: absolute; left: 612px; top: 352px; font-family: "Noto Sans SC", sans-serif; display: flex; align-items: baseline; gap: 10px; }
  .cn-name__person { color: var(--purple); font-size: 19px; }
  .cn-name__role { color: var(--green); font-size: 11px; }

  .website { position: absolute; right: 30px; top: 378px; font-size: 15px; }
</style>
</head>
<body>
  <div class="side-label side-label--front">Front:</div>
  <section class="card card--front">
    <div class="wordmark wordmark--front"><span class="wordmark__square"></span>Brantwell Media</div>
  </section>

  <div class="side-label side-label--back">Back:</div>
  <section class="card card--back">
    <div class="wordmark wordmark--back"><span class="wordmark__square"></span>Brantwell Media</div>

    <div class="swatches swatches--right">
      <span class="swatch swatch--green"></span>
      <span class="swatch swatch--purple"></span>
      <span class="swatch swatch--magenta"></span>
      <span class="swatch swatch--orange"></span>
    </div>

    <div class="contact">
      <div class="contact__name">Lena Zhou</div>
      <div class="contact__title">Account director</div>
      <div class="contact__cn">博文传媒咨询(北京)有限公司</div>
      <div class="contact__cn">北京市朝阳区新源里西路华茂商务中心C305 (100027)</div>
      <div>Suite <span class="hl-orange">C305</span>,Hua Mao Business Centre</div>
      <div>Xinyuanli West Rd Chaoyang District,Beijing <span class="hl-orange">100027</span></div>
      <div><span class="hl-magenta">Mobile:</span>+86 13800004217 <span class="hl-magenta">Email:</span>lena.zhou@brantwellmail.com</div>
      <div><span class="hl-magenta">Msn:</span>lena_zh@brantwellmail.com <span class="hl-orange">QQ:</span>1000234567</div>
    </div>

    <div class="swatches swatches--left">
      <span class="swatch swatch--green"></span>
      <span class="swatch swatch--purple"></span>
      <span class="swatch swatch--magenta"></span>
      <span class="swatch swatch--orange"></span>
    </div>

    <div class="cn-name"><span class="cn-name__person">周琳</span><span class="cn-name__role">客户总监</span></div>
    <div class="website">www.brantwellchina.com</div>
  </section>
</body>
</html>
```